Brisk Yard, LLC Web Design

I would like a web site design for a new lawn care business I am creating for my son. This is what it looks like now.

http://www.briskyardllc.example

Target Market(s)

Target customer is blue collar or middle class people who do not have time to do all of the Brisk Yard around their home such as mowing the lawn, clearing snow etc. Or they need help moving or moving something such as mulch or wood. Shoot for an economical audience that may not have thought about having these tasks done for them.

Industry/Entity Type

Lawn Care

Colors
acd037
9bcb3c
cadf82
eaf2cf

Requirements
Must have
• I put in greens below. The colors that were available were not the best greens or the greens I would think about. The greens on the web site are more close.
Nice to have
• Will have a few more pictures of the logo guy on different machines. Will upload as soon as I get.

```html
<!DOCTYPE html>
<html lang="en">
<head>
<meta charset="utf-8">
<title>Brisk Yard, LLC</title>
<link rel="stylesheet" href="https://fonts.googleapis.com/css2?family=Open+Sans:ital,wght@0,400;0,600;0,700;1,800&family=Arimo:wght@400;700&display=swap">
<style>
:root{
  --lime:#acd037;
  --leaf:#9bcb3c;
  --pale:#cadf82;
  --mist:#eaf2cf;
  --forest:#2f8a1c;
  --ink:#222;
  --body:#333;
  --panel:#f5f5f5;
  --white:#fff;
}
*{margin:0;padding:0;box-sizing:border-box}
html,body{width:1098px;height:1200px;overflow:hidden;background:var(--white)}
body{position:relative;font-family:"Arimo",Arial,sans-serif;color:var(--body)}
.top-band{position:absolute;left:0;top:0;width:1098px;height:393px;background:linear-gradient(#cde24a,#8fc03a 55%,#6fa925)}
.stage{position:absolute;left:141px;top:43px;width:817px;height:498px;background:var(--panel);box-shadow:0 6px 8px -4px rgba(0,0,0,.18)}
.brand{position:absolute;left:173px;top:25px;width:236px;height:107px;background:var(--lime);border:2px solid #d8ea9a;display:flex;align-items:center;justify-content:center;gap:9px;box-shadow:2px 3px 5px rgba(0,0,0,.2);z-index:2}
.brand-dot{width:24px;height:24px;border-radius:50%;background:var(--forest);flex:none}
.brand-name{font-family:"Open Sans",sans-serif;font-weight:700;font-size:20px;color:var(--forest);white-space:nowrap}
.brand-fold{position:absolute;left:409px;top:26px;width:0;height:0;border-left:18px solid #2d3b12;border-top:16px solid transparent}
.nav{position:absolute;left:446px;top:57px;display:flex;align-items:center;font-size:10.5px;color:#444;text-transform:uppercase}
.nav a{color:inherit;text-decoration:none;margin-right:29px;line-height:30px}
.nav a.current{background:var(--leaf);color:var(--white);padding:0 12px;margin-right:18px}
.hero{position:absolute;left:174px;top:102px;width:752px;height:402px;background:linear-gradient(#a9d26a,#86bd3a 55%,#77b12c)}
.hero-title{position:absolute;left:0;width:100%;top:272px;text-align:center;font-family:"Open Sans",sans-serif;font-style:italic;font-weight:800;font-size:42px;color:var(--white);text-shadow:0 1px 3px rgba(0,0,0,.3)}
.hero-sub{position:absolute;left:0;width:100%;top:342px;text-align:center;font-family:"Arimo",Arial,sans-serif;font-size:21px;color:var(--white);text-shadow:0 1px 2px rgba(0,0,0,.3)}
.pager{position:absolute;left:535px;top:516px;display:flex;gap:6px}
.pager span{width:12px;height:12px;border-radius:50%;background:#2a2a2a;border:2px solid #ddd}
.pager span.on{background:var(--leaf)}
.welcome{position:absolute;left:174px;top:561px;width:752px;text-align:center}
.welcome h1{font-family:"Open Sans",sans-serif;font-weight:400;font-size:23px;color:var(--ink)}
.welcome h1 em{font-style:normal;color:var(--forest)}
.welcome p{margin-top:9px;font-size:9.6px;line-height:17.5px;color:#333}
.service{position:absolute;top:673px;width:236px}
.service-photo{width:236px;height:161px;border:2px solid var(--pale);box-shadow:0 0 0 1px #e4e4e4}
.service h2{margin-top:12px;font-family:"Open Sans",sans-serif;font-weight:400;font-size:14px;color:var(--ink)}
.service p{margin-top:5px;font-size:9.2px;line-height:17.4px;text-align:justify;color:#333}
.promo{position:absolute;left:174px;top:967px;width:752px;height:143px;display:flex}
.promo-photo{width:416px;height:143px;background:linear-gradient(160deg,#5a2a2a,#9a3030 55%,#7a2828)}
.promo-body{flex:1;background:var(--mist);text-align:center;padding-top:13px}
.promo-body h3{font-family:"Open Sans",sans-serif;font-weight:400;font-size:19px;color:var(--ink)}
.promo-body p{margin-top:9px;font-family:"Open Sans",sans-serif;font-size:10px;line-height:18.5px;color:#222}
.promo-body a{display:inline-block;margin-top:10px;width:131px;line-height:34px;background:var(--leaf);color:var(--white);font-family:"Open Sans",sans-serif;font-weight:600;font-size:13px;text-decoration:none}
.footer{position:absolute;left:0;top:1137px;width:1098px;height:63px;background:var(--leaf)}
.footer-copy{position:absolute;left:173px;top:26px;font-size:8.5px;font-weight:700;color:var(--white);text-transform:uppercase}
.social{position:absolute;left:483px;top:22px;display:flex;gap:6px}
.social span{width:18px;height:18px;border-radius:50%;background:#3b6fb0}
.footer-nav{position:absolute;left:610px;top:26px;font-size:8.5px;font-weight:700;color:var(--white);text-transform:uppercase;word-spacing:1px}
.footer-nav a{color:inherit;text-decoration:none}
.footer-nav i{font-style:normal;margin:0 8px}
</style>
</head>
<body>
<div class="top-band"></div>
<div class="stage"></div>

<div class="brand-fold"></div>
<div class="brand"><span class="brand-dot"></span><span class="brand-name">Brisk Yard, LLC</span></div>

<nav class="nav">
  <a class="current" href="#">Home</a>
  <a href="#">Lawn Care</a>
  <a href="#">Snow Removal</a>
  <a href="#">Yard Care</a>
  <a href="#">Contact</a>
  <a href="#">Schedule</a>
</nav>

<div class="hero" role="img" aria-label="Photo of a wide freshly mown lawn with trees under a blue sky">
  <div class="hero-title">HIGH QUALITY</div>
  <div class="hero-sub">MOWERS TO FIT ANY LAWN'S NEEDS!</div>
</div>
<div class="pager"><span></span><span></span><span class="on"></span></div>

<section class="welcome">
  <h1>Welcome To <em>Brisk Yard</em></h1>
  <p>Brisk Yard, LLC is the vision of Dale Harrow, owner and main worker. For the last 10 years he has been helping people by cutting their lawn, removing snow, cleaning yards or even just moving firewood, mulch or stones.&nbsp; He felt that it was time to take it to the next level and Brisk Yard, LLC was born. Brisk Yard, LLC is a locally owned business head-quartered in Fox Hollow, WI. Dale takes personal pride in providing cost effective and timely services to his clients.</p>
</section>

<article class="service" style="left:174px">
  <div class="service-photo" role="img" aria-label="Photo of a push mower cutting a green lawn" style="background:linear-gradient(#8cbf4a,#6fa532)"></div>
  <h2>Cutting their lawn</h2>
  <p>Brisk Yard, LLC uses lawn mowing technique's that leave a well manicured look. Understanding the impor-tance of how to maintain a healthy lawn comes with time, but there are proper practices</p>
</article>
<article class="service" style="left:432px">
  <div class="service-photo" role="img" aria-label="Photo of a snow blower clearing fresh snow" style="background:linear-gradient(#eef1f4,#cfd5db)"></div>
  <h2>Removing snow</h2>
  <p>Brisk Yard, LLC uses lawn mowing technique's that leave a well manicured look. Understanding the impor-tance of how to maintain a healthy lawn comes with time, but there are proper practices</p>
</article>
<article class="service" style="left:690px">
  <div class="service-photo" role="img" aria-label="Photo of two workers with yard equipment in a garage" style="background:linear-gradient(#6b6a3c,#4a4730)"></div>
  <h2>Cleaning yards</h2>
  <p>Brisk Yard, LLC uses lawn mowing technique's that leave a well manicured look. Understanding the impor-tance of how to maintain a healthy lawn comes with time, but there are proper practices</p>
</article>

<section class="promo">
  <div class="promo-photo" role="img" aria-label="Photo of two workers standing in front of a red pickup truck"></div>
  <div class="promo-body">
    <h3>CHOOSE A SERVICE</h3>
    <p>When snow removal stops and spring and summer arrives it<br>time to Call Brisk Yard, LLC.</p>
    <a href="#">Booking Now</a>
  </div>
</section>

<footer class="footer">
  <div class="footer-copy">&copy;2014 2014&nbsp; Brisk Yard, LLC, All Rights Reserved.</div>
  <div class="social" aria-label="Social links"><span></span><span></span><span></span></div>
  <div class="footer-nav"><a href="#">Home</a><i>|</i><a href="#">Lawn Care</a><i>|</i><a href="#">Snow Removal</a> | <a href="#">Yard Care</a><i>|</i><a href="#">Contact Us</a></div>
</footer>
</body>
</html>
```